Korean Homemade food restaurant just like what your mom cooks at home

I need a black and white simple and modern design according to my logo.
My restaurant name is Noru Kan (meaning of home cooking).
I need to have 솔찬(Noru Kan) in Korean need to be included. Once again 솔찬.
I am not sure if I need to include my name and number and adress.

솔찬 Noru Kan 418 Marlow Ct. Clarksville, TN 37512 Grant Oh Owner Cell:931-555-0183 Store:931-555-0297

Target Market(s)

business owners, university students

Industry/Entity Type

Restaurant

Contact Information for Business Card

This is traditional Korean food restaurant that targets university students during lunch and Korean business travelers at dinner.

Font styles to use
Sans Serif

Requirements
Must have
• Must have my logo.

```html
<!DOCTYPE html>
<html lang="en">
<head>
<meta charset="utf-8">
<title>Noru Kan – Business Card</title>
<link rel="stylesheet" href="https://fonts.googleapis.com/css2?family=Noto+Sans+KR:wght@400&family=Saira:wght@400;500;600&display=swap">
<style>
  :root {
    --page-bg: #d8d4ce;
    --card-bg: #eeeae4;
    --card-edge: #c9c4bc;
    --ink: #2e2e30;
    --ink-soft: #3b3b3d;
    --accent-blue: #3e3f9c;
    --rule: #8e8c92;
    --band-dark: #242426;
    --band-grey: #b3b2b8;
    --band-text: #ffffff;
  }
  * { margin: 0; padding: 0; box-sizing: border-box; }
  html, body {
    width: 1200px; height: 768px; overflow: hidden;
    background: var(--page-bg);
    font-family: "Saira", sans-serif;
  }
  .card {
    position: absolute; left: 60px; top: 70px;
    width: 1080px; height: 627px;
    background: linear-gradient(160deg, #f3f0ec 0%, var(--card-bg) 60%, #e6e1da 100%);
    border: 2px solid var(--card-edge);
    border-radius: 32px;
    overflow: hidden;
    box-shadow: 0 14px 40px rgba(0,0,0,0.12);
    color: var(--ink);
  }
  .holder-name {
    position: absolute; left: 44px; top: 208px;
    font-size: 30px; font-weight: 500; letter-spacing: 1.5px;
    color: var(--ink-soft);
  }
  .holder-title {
    position: absolute; left: 44px; top: 257px;
    font-size: 24px; font-weight: 500; letter-spacing: 0.5px;
    color: var(--accent-blue);
  }
  .divider {
    position: absolute; left: 64px; top: 308px;
    width: 940px; height: 3px;
    background: linear-gradient(90deg, rgba(142,140,146,0.15), var(--rule) 30%, var(--rule) 70%, rgba(142,140,146,0.2));
  }
  .brand {
    position: absolute; right: 78px; top: 52px;
    display: flex; flex-direction: column; align-items: center;
  }
  .brand-korean {
    font-family: "Noto Sans KR", "Saira", sans-serif;
    font-size: 66px; font-weight: 400; line-height: 1.2;
    color: var(--ink);
    margin-bottom: 14px;
  }
  .brand-row {
    display: flex; align-items: center; gap: 18px;
  }
  .brand-dot {
    width: 22px; height: 22px; border-radius: 50%;
    background: var(--ink);
  }
  .brand-name {
    font-size: 72px; font-weight: 400; line-height: 1;
    color: var(--ink);
  }
  .address {
    position: absolute; left: 44px; top: 410px;
    font-style: normal;
    font-size: 22px; line-height: 35px; letter-spacing: 0.6px;
    color: var(--ink-soft);
  }
  .contact-list {
    position: absolute; right: 34px; top: 332px;
    list-style: none;
    text-align: right;
  }
  .contact-item {
    display: flex; justify-content: flex-end; align-items: center;
    gap: 14px;
    font-size: 21px; letter-spacing: 1px; color: var(--ink-soft);
    height: 52px;
  }
  .contact-item.small { font-size: 19px; height: 37px; letter-spacing: 0.3px; }
  .contact-item svg { width: 24px; height: 24px; flex: none; fill: var(--ink-soft); }
  .bottom-band {
    position: absolute; left: 0; bottom: 0; width: 1080px; height: 70px;
  }
  .band-web {
    position: absolute; left: 44px; bottom: 14px;
    font-size: 20px; font-weight: 500; letter-spacing: 0.8px;
    color: var(--band-text);
  }
</style>
</head>
<body>
  <main class="card">
    <h1 class="holder-name">WREN TALLEY</h1>
    <p class="holder-title">Managing Director</p>

    <div class="brand">
      <span class="brand-korean" lang="ko">솔찬</span>
      <div class="brand-row">
        <span class="brand-dot"></span>
        <span class="brand-name">Noru Kan</span>
      </div>
    </div>

    <div class="divider"></div>

    <address class="address">
      27 Harlow Ln, 4th floor<br>
      Bellmont Row BKR
    </address>

    <ul class="contact-list">
      <li class="contact-item">931 555 0164
        <svg viewBox="0 0 24 24" aria-hidden="true"><path d="M6.6 10.8a15.1 15.1 0 0 0 6.6 6.6l2.2-2.2c.3-.3.7-.4 1-.2 1.1.4 2.3.6 3.6.6.6 0 1 .4 1 1V20c0 .6-.4 1-1 1C10.6 21 3 13.4 3 4c0-.6.4-1 1-1h3.5c.6 0 1 .4 1 1 0 1.3.2 2.5.6 3.6.1.3 0 .7-.2 1z"/></svg>
      </li>
      <li class="contact-item">931 555 0164
        <svg viewBox="0 0 24 24" aria-hidden="true"><path d="M7 1h10a2 2 0 0 1 2 2v18a2 2 0 0 1-2 2H7a2 2 0 0 1-2-2V3a2 2 0 0 1 2-2zm0 3v14h10V4zm5 15.2a1.1 1.1 0 1 0 0 2.2 1.1 1.1 0 0 0 0-2.2z"/></svg>
      </li>
      <li class="contact-item">931 555 0164
        <svg viewBox="0 0 24 24" aria-hidden="true"><path d="M3 8h3v14H3zM8 3h9l3 3v16H8zm2 2v5h8V7h-3V5zm1 8v2h2v-2zm4 0v2h2v-2zm-4 4v2h2v-2zm4 0v2h2v-2z"/></svg>
      </li>
      <li class="contact-item small">hello@norukan.com
        <svg viewBox="0 0 24 24" aria-hidden="true"><path d="M2 5h20v14H2zm2 2v.4l8 5.2 8-5.2V7zm0 2.8V17h16V9.8l-8 5.2z"/></svg>
      </li>
      <li class="contact-item small">www.norukankitchen.com
        <svg viewBox="0 0 24 24" aria-hidden="true"><path d="M12 2a10 10 0 1 0 0 20 10 10 0 0 0 0-20zm6.9 6h-2.9a15 15 0 0 0-1.3-3.6A8 8 0 0 1 18.9 8zM12 4c.8 1.1 1.5 2.5 1.9 4h-3.8c.4-1.5 1.1-2.9 1.9-4zM4.3 14a8.2 8.2 0 0 1 0-4h3.3a16 16 0 0 0 0 4zm.8 2h2.9c.3 1.3.8 2.5 1.3 3.6A8 8 0 0 1 5.1 16zM8 8H5.1a8 8 0 0 1 4.2-3.6C8.8 5.5 8.3 6.7 8 8zm4 12c-.8-1.1-1.5-2.5-1.9-4h3.8c-.4 1.5-1.100 2.9-1.9 4zm2.3-6H9.7a14 14 0 0 1 0-4h4.6a14 14 0 0 1 0 4zm.4 5.6c.5-1.1 1-2.3 1.3-3.6h2.9a8 8 0 0 1-4.2 3.6zm1.7-5.6a16 16 0 0 0 0-4h3.3a8.2 8.2 0 0 1 0 4z"/></svg>
      </li>
    </ul>

    <svg class="bottom-band" viewBox="0 0 1080 70" preserveAspectRatio="none" aria-hidden="true">
      <rect x="0" y="23" width="1080" height="47" fill="var(--band-grey)"/>
      <path d="M0 0 H405 C430 0 440 20 448 40 C455 60 462 70 470 70 H0 Z" fill="var(--band-dark)"/>
    </svg>
    <span class="band-web">www.norukankitchen.com</span>
  </main>
</body>
</html>
```